Stationery Design for a fast food resturaunt

We just created our logo, we need nice stationary to go with it. We beed the design to be on white background and black background.

Target Market(s)

Landlords who will lease their retail shops to us. Shopping Mall Management.Real Estate Professionals.

Font styles to use
Sans Serif

```html
<!DOCTYPE html>
<html lang="en">
<head>
<meta charset="utf-8">
<title>Amber Hive Stationery</title>
<link rel="stylesheet" href="https://fonts.googleapis.com/css2?family=Lato:wght@300;400&display=swap">
<style>
  :root {
    --bg: #e9e9e9;
    --paper: #ffffff;
    --amber: #fcb415;
    --charcoal: #3d3d3d;
    --edge: #dcdcdc;
  }
  * { box-sizing: border-box; margin: 0; padding: 0; }
  html, body { width: 1200px; height: 834px; overflow: hidden; }
  body {
    background: var(--bg);
    font-family: "Lato", Arial, sans-serif;
    position: relative;
  }
  .sheet {
    position: absolute;
    background: var(--paper);
    border: 1px solid var(--edge);
    overflow: hidden;
  }
  .brand {
    position: absolute;
    display: flex;
    align-items: center;
    gap: 8px;
    color: var(--amber);
    font-weight: 300;
    letter-spacing: 1px;
    white-space: nowrap;
  }
  .brand-square {
    background: var(--charcoal);
    flex: none;
  }
  .rule-thin, .rule-thick {
    position: absolute;
    left: 0;
    right: 0;
    background: var(--amber);
  }

  /* Letterhead */
  .letterhead { left: 116px; top: 80px; width: 460px; height: 644px; }
  .letterhead .brand { top: 22px; left: 50%; transform: translateX(-50%); font-size: 34px; }
  .letterhead .brand-square { width: 22px; height: 22px; }
  .letterhead .rule-thin { top: 574px; height: 5px; }
  .letterhead .rule-thick { top: 594px; height: 19px; }
  .letterhead-footer {
    position: absolute; top: 621px; left: 0; right: 0;
    text-align: center; color: var(--amber); font-size: 11px; font-weight: 400;
  }

  /* Business card front */
  .card-front { left: 634px; top: 79px; width: 183px; height: 106px; border-left: 5px solid var(--amber); }
  .card-front .brand { top: 38px; left: 50%; transform: translateX(-50%); font-size: 20px; gap: 6px; }
  .card-front .brand-square { width: 13px; height: 13px; }

  /* Business card back */
  .card-back { left: 888px; top: 82px; width: 182px; height: 104px; }
  .card-back .brand-square { position: absolute; left: 0; top: 16px; width: 34px; height: 34px; }
  .contact-list {
    position: absolute; left: 53px; top: 22px; list-style: none;
    color: var(--amber); font-size: 11px; line-height: 14px; font-weight: 400;
  }

  /* Compliment slip */
  .slip { left: 636px; top: 244px; width: 434px; height: 218px; }
  .slip .brand { top: 12px; left: 8px; font-size: 22px; gap: 6px; }
  .slip .brand-square { width: 14px; height: 14px; }
  .slip-heading {
    position: absolute; top: 76px; left: 0; right: 0; text-align: center;
    color: var(--amber); font-size: 20px; font-weight: 400;
  }
  .slip-details {
    position: absolute; top: 100px; left: 0; right: 0; text-align: center;
    color: var(--amber); font-size: 10px; line-height: 12px; font-weight: 400;
  }
  .slip .rule-thin { top: 162px; height: 5px; }
  .slip .rule-thick { top: 181px; height: 18px; }

  /* Envelope */
  .envelope { left: 636px; top: 504px; width: 436px; height: 218px; }
  .envelope-flap { position: absolute; left: 0; top: 0; width: 436px; height: 92px; }
  .envelope .brand { top: 8px; left: 50%; transform: translateX(-50%); font-size: 22px; gap: 6px; }
  .envelope .brand-square { width: 14px; height: 14px; }
  .envelope .rule-thin { top: 170px; height: 5px; }
  .envelope .rule-thick { top: 186px; height: 18px; }
</style>
</head>
<body>

  <section class="sheet letterhead">
    <div class="brand"><span class="brand-name">AMBER HIVE</span><span class="brand-square"></span></div>
    <div class="rule-thin"></div>
    <div class="rule-thick"></div>
    <p class="letterhead-footer">(555) 010 - 2468 - City, Country - Email Address</p>
  </section>

  <section class="sheet card-front">
    <div class="brand"><span class="brand-name">AMBER HIVE</span><span class="brand-square"></span></div>
  </section>

  <section class="sheet card-back">
    <span class="brand-square"></span>
    <ul class="contact-list">
      <li>PERSON'S NAME</li>
      <li>Telephone</li>
      <li>Email</li>
      <li>Mailing</li>
    </ul>
  </section>

  <section class="sheet slip">
    <div class="brand"><span class="brand-name">AMBER HIVE</span><span class="brand-square"></span></div>
    <h2 class="slip-heading">BIG NAME</h2>
    <p class="slip-details">FOLLOWED BY<br>ALL OF THEIR<br>INFORMATION</p>
    <div class="rule-thin"></div>
    <div class="rule-thick"></div>
  </section>

  <section class="sheet envelope">
    <svg class="envelope-flap" viewBox="0 0 436 92" aria-hidden="true">
      <path d="M0 2 Q218 150 436 2" fill="none" stroke="#e2e2e2" stroke-width="1.5"/>
    </svg>
    <div class="brand"><span class="brand-name">AMBER HIVE</span><span class="brand-square"></span></div>
    <div class="rule-thin"></div>
    <div class="rule-thick"></div>
  </section>

</body>
</html>
```